Brindlow Legal Business Card

I require a corporate business card for a new legal services business.

I do not have a logo, nor do I want one.

I require a clean, neat a professional card for a law firm.

Details:

Business Name: Brindlow Legal
Name: Delia ter Hulst
Title: Corporate Services Manager
Location: Office 14 (Top Floor), Kelvara Business Centre, Dunmore Ash Street, Korimba CBD, Tarrow Bay Province.
Postal Address: PO Box 537, Korimba, 418, Tarrow Bay Province, Vantuel Islands.
Contact: T: +675 6428153, F: +675 6427602, M: +675 79154368, E: dterhulst@brindlowqx.com.pg.

I look forward to your design submissions.

Legal

```html
<!DOCTYPE html>
<html lang="en">
<head>
<meta charset="utf-8">
<title>Brindlow Legal – Business Card</title>
<link href="https://fonts.googleapis.com/css2?family=Montserrat:wght@500;600;700&display=swap" rel="stylesheet">
<style>
  :root {
    --navy: #0d3466;
    --navy-deep: #0a2c5a;
    --paper: #ffffff;
    --backdrop: #e6e7ea;
    --band-text: #e9eef6;
  }
  * { margin: 0; padding: 0; box-sizing: border-box; }
  html, body {
    width: 1200px; height: 900px; overflow: hidden;
    background: var(--backdrop);
    font-family: "Montserrat", Arial, sans-serif;
    color: var(--navy);
  }
  .card {
    position: absolute; left: 75px; top: 150px;
    width: 1050px; height: 600px;
    background: var(--paper);
    box-shadow: 0 6px 24px rgba(0,0,0,0.12);
    overflow: hidden;
  }
  .firm-name {
    position: absolute; left: 92px; right: 92px; top: 96px;
    font-size: 64px; font-weight: 700;
    letter-spacing: 0.18em; line-height: 1;
    white-space: nowrap;
  }
  .person {
    position: absolute; left: 92px; right: 92px; top: 220px;
    display: flex; align-items: center; gap: 22px;
  }
  .rule { flex: 1; height: 2px; background: var(--navy); }
  .rule--left { margin-top: 34px; }
  .rule--right { margin-top: -20px; }
  .person-id { text-align: center; }
  .person-name { font-size: 32px; font-weight: 600; line-height: 1.1; }
  .person-title { font-size: 17px; font-weight: 500; margin-top: 4px; }
  .office-address {
    position: absolute; right: 92px; top: 300px;
    text-align: right; font-size: 19px; font-weight: 500; line-height: 1.45;
    font-style: normal;
  }
  .contacts {
    position: absolute; left: 92px; top: 364px;
    font-size: 20px; font-weight: 500; line-height: 1.5;
    list-style: none;
  }
  .contact-label { display: inline-block; width: 34px; }
  .postal-band {
    position: absolute; left: 0; right: 0; bottom: 0; height: 96px;
    background: var(--navy-deep);
    display: flex; align-items: center; padding-left: 150px;
    color: var(--band-text); font-size: 21px; font-weight: 500;
  }
</style>
</head>
<body>
  <main class="card">
    <h1 class="firm-name">BRINDLOW LEGAL</h1>

    <div class="person">
      <span class="rule rule--left"></span>
      <div class="person-id">
        <p class="person-name">Delia ter Hulst</p>
        <p class="person-title">Corporate Services Manager</p>
      </div>
      <span class="rule rule--right"></span>
    </div>

    <address class="office-address">
      Office 14 (Top Floor)<br>
      Kelvara Business Centre<br>
      Dunmore Ash St., Korimba CBD<br>
      Tarrow Bay Province
    </address>

    <ul class="contacts">
      <li><span class="contact-label">P :</span>+675 642 8153</li>
      <li><span class="contact-label">F :</span>+675 642 7602</li>
      <li><span class="contact-label">M:</span>+675 791 54368</li>
      <li><span class="contact-label">E :</span>dterhulst@brindlowqx.com.pg</li>
    </ul>

    <footer class="postal-band">PO Box 537, Korimba, 418, Tarrow Bay Province, Vantuel Islands</footer>
  </main>
</body>
</html>
```